Brevik Fabrication - Business Card Design

We would like a dark (likely black) themed business card to be able to hand out to potential clients. We may list our services on the card or keep it clean. Unsure. Logo attached

```html
<!DOCTYPE html>
<html lang="en">
<head>
<meta charset="utf-8">
<title>Brevik Fabrication – Business Card Design</title>
<link rel="stylesheet" href="https://fonts.googleapis.com/css2?family=Poppins:wght@300;400;600;700&display=swap">
<style>
  :root{
    --header-bg:#3a393b;
    --sheet-top:#f3f3f3;
    --sheet-bottom:#e8e9eb;
    --divider:#555457;
    --pill:#3a393b;
    --card:#040608;
    --ink:#ffffff;
    --brand-blue:#1c75bc;
    --brand-orange:#f15a24;
    --ghost:rgba(255,255,255,0.06);
  }
  *{margin:0;padding:0;box-sizing:border-box;}
  html,body{width:849px;height:1200px;overflow:hidden;}
  body{position:relative;font-family:"Poppins",sans-serif;background:var(--sheet-bottom);color:var(--ink);}

  .header{position:absolute;left:0;top:0;width:849px;height:161px;background:var(--header-bg);text-align:center;}
  .header__title{position:absolute;left:0;right:0;top:21px;font-size:23px;font-weight:700;letter-spacing:0.2px;}
  .header__brand{position:absolute;left:0;right:0;top:86px;display:flex;flex-direction:column;align-items:center;gap:5px;}

  .sheet-top{position:absolute;left:0;top:161px;width:849px;height:524px;background:var(--sheet-top);}
  .sheet-bottom{position:absolute;left:0;top:685px;width:849px;height:515px;background:var(--sheet-bottom);}
  .divider{position:absolute;left:422px;top:161px;width:1px;height:1001px;background:var(--divider);}

  .pill{position:absolute;width:95px;height:42px;border-radius:21px;background:var(--pill);color:var(--ink);
        font-size:13px;font-weight:300;display:flex;align-items:center;justify-content:center;}

  .card{position:absolute;background:var(--card);overflow:hidden;}
  .card--wide{width:300px;height:171px;}
  .card--tall{width:171px;height:299px;}
  .card--round{border-radius:9px;}

  .ghost-mark{position:absolute;background:radial-gradient(ellipse at center,var(--ghost) 0%,rgba(255,255,255,0.035) 45%,rgba(255,255,255,0) 72%);}

  .brand{position:absolute;display:flex;flex-direction:column;align-items:center;}
  .brand__dot{border-radius:50%;background:var(--brand-orange);}
  .brand__name{font-weight:700;color:var(--brand-blue);text-transform:uppercase;white-space:nowrap;line-height:1;}

  .contact{position:absolute;font-size:7.6px;font-weight:400;line-height:1.25;}
  .contact__name{font-size:15.5px;font-weight:400;line-height:1;}
  .contact__role{font-size:7.4px;font-weight:600;letter-spacing:0.2px;margin-top:2px;}
  .contact__row{display:flex;align-items:flex-start;gap:3px;}
  .contact__row svg{flex:none;margin-top:1px;}

  .contact--tall{left:0;width:171px;text-align:center;}
  .contact--tall .contact__name{font-size:17px;}
  .web-band{position:absolute;left:0;bottom:0;width:171px;height:25px;background:var(--brand-blue);
            font-size:7.8px;display:flex;align-items:center;justify-content:center;padding-bottom:3px;}
</style>
</head>
<body>

<header class="header">
  <h1 class="header__title">BUSINESS CARD DESIGN</h1>
  <div class="header__brand">
    <span class="brand__name" style="font-size:13px;">Brevik Fabrication</span>
  </div>
</header>

<div class="sheet-top"></div>
<div class="sheet-bottom"></div>
<div class="divider"></div>

<!-- Option 1 -->
<div class="pill" style="left:166px;top:208px;">OPTION 1</div>

<div class="card card--wide" style="left:71px;top:277px;">
  <div class="ghost-mark" role="img" aria-label="Faint enlarged brand mark decoration" style="left:-20px;top:-10px;width:210px;height:190px;"></div>
  <div class="brand" style="left:0;top:40px;width:164px;gap:10px;">
    <span class="brand__dot" style="width:40px;height:40px;"></span>
    <span class="brand__name" style="font-size:12.5px;">Brevik Fabrication</span>
  </div>
  <div class="contact" style="left:165px;top:34px;">
    <div class="contact__name">Elena Marsh</div>
    <div class="contact__role">FINANCIAL ANALYST</div>
    <div class="contact__row" style="margin-top:18px;">
      <svg width="6" height="6" viewBox="0 0 24 24" aria-hidden="true"><path fill="#fff" d="M6.6 10.8a15.2 15.2 0 0 0 6.6 6.6l2.2-2.2a1 1 0 0 1 1-.25 11.4 11.4 0 0 0 3.6.57 1 1 0 0 1 1 1V20a1 1 0 0 1-1 1A17 17 0 0 1 3 4a1 1 0 0 1 1-1h3.5a1 1 0 0 1 1 1c0 1.25.2 2.45.57 3.6a1 1 0 0 1-.25 1z"/></svg>
      <span>+1 555 014 2230</span>
    </div>
    <div class="contact__row" style="margin-top:8px;">
      <svg width="6" height="7" viewBox="0 0 24 28" aria-hidden="true"><path fill="#fff" d="M12 0a10 10 0 0 0-10 10c0 7.5 10 18 10 18s10-10.5 10-18A10 10 0 0 0 12 0zm0 14a4 4 0 1 1 0-8 4 4 0 0 1 0 8z"/></svg>
      <span>88 Harbor Lane<br>Portview, OR 97031</span>
    </div>
    <div style="margin-top:9px;">elena@brevikfab.com<br>www.brevikfab.com</div>
  </div>
</div>

<div class="card card--wide" style="left:71px;top:457px;">
  <div class="brand" style="left:0;top:32px;width:300px;gap:16px;">
    <span class="brand__dot" style="width:62px;height:62px;"></span>
    <span class="brand__name" style="font-size:19px;">Brevik Fabrication</span>
  </div>
</div>

<!-- Option 2 -->
<div class="pill" style="left:586px;top:208px;">OPTION 2</div>

<div class="card card--wide card--round" style="left:476px;top:277px;">
  <div class="ghost-mark" role="img" aria-label="Faint enlarged brand mark decoration" style="left:-20px;top:-10px;width:200px;height:190px;"></div>
  <div class="brand" style="left:0;top:40px;width:145px;gap:8px;">
    <span class="brand__dot" style="width:78px;height:78px;"></span>
    <span class="brand__name" style="font-size:10px;">Brevik Fabrication</span>
  </div>
  <div class="contact" style="left:165px;top:34px;">
    <div class="contact__name">Elena Marsh</div>
    <div class="contact__role">FINANCIAL ANALYST</div>
    <div style="margin-top:18px;">+1 555 014 2230</div>
    <div style="margin-top:8px;">88 Harbor Lane<br>Portview, OR 97031</div>
    <div style="margin-top:9px;">elena@brevikfab.com<br>www.brevikfab.com</div>
  </div>
</div>

<div class="card card--wide card--round" style="left:476px;top:457px;">
  <div class="brand" style="left:0;top:32px;width:300px;gap:16px;">
    <span class="brand__dot" style="width:62px;height:62px;"></span>
    <span class="brand__name" style="font-size:19px;">Brevik Fabrication</span>
  </div>
</div>

<!-- Option 3 -->
<div class="pill" style="left:166px;top:730px;">OPTION 3</div>

<div class="card card--tall" style="left:46px;top:809px;">
  <div class="ghost-mark" role="img" aria-label="Faint enlarged brand mark decoration" style="left:-10px;top:110px;width:190px;height:190px;"></div>
  <div class="brand" style="left:0;top:25px;width:171px;gap:6px;">
    <span class="brand__dot" style="width:44px;height:44px;"></span>
    <span class="brand__name" style="font-size:9px;">Brevik Fabrication</span>
  </div>
  <div class="contact contact--tall" style="top:105px;">
    <div class="contact__name">Elena Marsh</div>
    <div class="contact__role">FINANCIAL ANALYST</div>
    <div style="margin-top:13px;">+1 555 014 2230<br>+1 555 014 2231</div>
    <div style="margin-top:10px;">88 Harbor Lane<br>Portview, OR 97031</div>
    <div style="margin-top:11px;">elena@brevikfab.com</div>
  </div>
  <div class="web-band">www.brevikfab.com</div>
</div>

<div class="card card--tall" style="left:224px;top:809px;">
  <div class="ghost-mark" role="img" aria-label="Faint enlarged brand mark decoration" style="left:-5px;top:15px;width:181px;height:270px;"></div>
  <div class="brand" style="left:0;top:106px;width:171px;gap:10px;">
    <span class="brand__dot" style="width:42px;height:42px;"></span>
    <span class="brand__name" style="font-size:11.5px;">Brevik Fabrication</span>
  </div>
</div>

<!-- Option 4 -->
<div class="pill" style="left:586px;top:730px;">OPTION 4</div>

<div class="card card--tall card--round" style="left:448px;top:809px;">
  <div class="ghost-mark" role="img" aria-label="Faint enlarged brand mark decoration" style="left:-10px;top:110px;width:190px;height:190px;"></div>
  <div class="brand" style="left:0;top:25px;width:171px;gap:6px;">
    <span class="brand__dot" style="width:44px;height:44px;"></span>
    <span class="brand__name" style="font-size:9px;">Brevik Fabrication</span>
  </div>
  <div class="contact contact--tall" style="top:105px;">
    <div class="contact__name">Elena Marsh</div>
    <div class="contact__role">FINANCIAL ANALYST</div>
    <div style="margin-top:13px;">+1 555 014 2230<br>+1 555 014 2231</div>
    <div style="margin-top:10px;">88 Harbor Lane<br>Portview, OR 97031</div>
    <div style="margin-top:11px;">elena@brevikfab.com</div>
  </div>
  <div class="web-band">www.brevikfab.com</div>
</div>

<div class="card card--tall card--round" style="left:632px;top:809px;">
  <div class="ghost-mark" role="img" aria-label="Faint enlarged brand mark decoration" style="left:-5px;top:15px;width:181px;height:230px;"></div>
  <div class="brand" style="left:0;top:106px;width:171px;gap:10px;">
    <span class="brand__dot" style="width:42px;height:42px;"></span>
    <span class="brand__name" style="font-size:11.5px;">Brevik Fabrication</span>
  </div>
</div>

</body>
</html>
```